Sleek and elegant promotional banner/sign for The Belvane Law Firm

We need a design for promotional items like banners, signs, print ads, etc. that includes our firm name - "The Belvane Law Firm" - and what we do. We advise businesses and individuals on legal matters; we represent individuals and businesses in litigation and transactions; we select and create business entities; we solve legal problems for individuals and businesses, etc. PLEASE DO NOT SIMPLY REPEAT THE PREVIOUS SENTENCE ON THE DESIGN. Please create a tag-line or brief description from ours. We need something that describes what we do in concise and creative manner while communicating trust and confidence. The banner must also include our basic contact information: 818.452-7196 (telephone) and belvanelaw.example (website). You may use one or more of the attached images, but needn't use any with the right design. The design should be sleek and modern.

Target Market(s)

wealthy individuals and small business owners, entrepreneurs

Industry/Entity Type

Lawyer

Font styles to use
Sans Serif

Colors
33a6d7
0556a4
33b8a4

Requirements
Must have
• Firm name, contact information, BRIEF description of our services, sleek and elegant.
• Also, the design must be horizontal - not vertical.
Nice to have
• I'd like to use one of the images
Should not have
• Cliches

```html
<!DOCTYPE html>
<html lang="en">
<head>
<meta charset="utf-8">
<title>The Belvane Law Firm – Banner</title>
<link href="https://fonts.googleapis.com/css2?family=Open+Sans:wght@600;700&family=Roboto+Condensed:wght@700&display=swap" rel="stylesheet">
<style>
  :root {
    --backdrop: #e4e5e7;
    --firm-blue: #0556a4;
    --firm-teal: #33b8a4;
    --white: #ffffff;
    --stone-light: #eeece8;
    --stone-mid: #c9c6c0;
    --stone-dark: #8f8c87;
  }
  * { margin: 0; padding: 0; box-sizing: border-box; }
  html, body {
    width: 1200px; height: 720px; overflow: hidden;
    background: var(--backdrop);
  }
  .banner {
    position: absolute; left: 27px; top: 131px;
    width: 1146px; height: 458px; overflow: hidden;
  }
  .banner__photo {
    position: absolute; inset: 0;
    background: linear-gradient(100deg, var(--stone-light) 0%, var(--stone-mid) 40%, var(--stone-light) 60%, var(--stone-dark) 100%);
  }
  .banner__shapes { position: absolute; inset: 0; }
  .firm-name {
    position: absolute; left: 640px; width: 490px; top: 38px;
    text-align: center; color: var(--white);
    font-family: "Open Sans", sans-serif; font-weight: 700;
    font-size: 58px; line-height: 1; letter-spacing: 1px;
  }
  .firm-sub {
    position: absolute; left: 640px; width: 492px; top: 104px;
    display: flex; align-items: center; gap: 12px;
    color: var(--white);
    font-family: "Open Sans", sans-serif; font-weight: 600;
    font-size: 31px; line-height: 1; white-space: nowrap;
  }
  .firm-sub__rule { flex: 1; height: 3px; background: var(--firm-teal); }
  .tagline {
    position: absolute; left: 630px; width: 486px; top: 168px;
    text-align: center;
    font-family: "Roboto Condensed", sans-serif; font-weight: 700;
    text-transform: uppercase; line-height: 1;
  }
  .tagline__lead { display: block; color: var(--firm-teal); font-size: 112px; letter-spacing: 1px; }
  .tagline__line { display: block; color: var(--white); }
  .tagline__line--large { font-size: 50px; margin-top: -2px; }
  .tagline__line--small { font-size: 38px; margin-top: 4px; }
  .contact {
    position: absolute; left: 446px; right: 24px; top: 386px; height: 72px;
    display: flex; align-items: center; gap: 12px;
    color: var(--white);
    font-family: "Open Sans", sans-serif; font-weight: 700;
  }
  .contact__phone { font-size: 33px; }
  .contact__web { font-size: 25px; }
  .contact__divider { width: 2px; height: 42px; background: var(--white); margin: 0 6px; }
  .contact__icon { width: 36px; height: 36px; flex: none; }
</style>
</head>
<body>
  <div class="banner">
    <div class="banner__photo" role="img" aria-label="Photograph of white marble courthouse columns above stone steps"></div>
    <svg class="banner__shapes" width="1146" height="458" viewBox="0 0 1146 458">
      <polygon points="630,0 1146,0 1146,458 512,458" fill="var(--white)"/>
      <polygon points="637,0 1146,0 1146,458 548,458" fill="var(--firm-blue)"/>
      <polygon points="442,386 1146,386 1146,458 412,458" fill="var(--firm-teal)"/>
    </svg>

    <div class="firm-name">THE BELVANE</div>
    <div class="firm-sub"><span class="firm-sub__rule"></span>LAW FIRM<span class="firm-sub__rule"></span></div>

    <h1 class="tagline">
      <span class="tagline__lead">We Solve</span>
      <span class="tagline__line tagline__line--large">Legal Problems For</span>
      <span class="tagline__line tagline__line--small">Individuals and Businesses</span>
    </h1>

    <div class="contact">
      <svg class="contact__icon" viewBox="0 0 36 36" aria-hidden="true">
        <circle cx="18" cy="18" r="16" fill="none" stroke="#fff" stroke-width="2.5"/>
        <path d="M12.5 10.5c1-.8 2-.6 2.6.3l1.6 2.4c.5.8.3 1.6-.4 2.2l-1 .8c.8 2 2.4 3.7 4.4 4.6l.9-1c.6-.7 1.5-.8 2.2-.3l2.4 1.6c.9.6 1 1.7.2 2.6l-1.2 1.2c-1 1-2.6 1.2-4 .5-4-2-7.2-5.2-9-9.2-.6-1.4-.3-3 .7-4z" fill="#fff"/>
      </svg>
      <span class="contact__phone">818.452-7196</span>
      <span class="contact__divider"></span>
      <svg class="contact__icon" viewBox="0 0 36 36" aria-hidden="true">
        <circle cx="18" cy="18" r="16" fill="none" stroke="#fff" stroke-width="2.5"/>
        <g fill="none" stroke="#fff" stroke-width="1.8">
          <circle cx="18" cy="18" r="10"/>
          <ellipse cx="18" cy="18" rx="4.5" ry="10"/>
          <line x1="8" y1="18" x2="28" y2="18"/>
          <line x1="9.5" y1="13" x2="26.5" y2="13"/>
          <line x1="9.5" y1="23" x2="26.5" y2="23"/>
        </g>
      </svg>
      <span class="contact__web">www.belvanelaw.example</span>
    </div>
  </div>
</body>
</html>
```